UI Improvement for FlorvaLink app

We are looking for a talented UI/UX designer to REFINE and enhance the visual design of our mobile application, FlorvaLink. The app is fully functional, but we need a designer to improve its aesthetics by specifying design elements such as fonts, colors, spacing, and component styles.
Your task will be to analyze the CURRENT UI and provide detailed design specifications that will make the app more visually appealing, modern, and user-friendly.
TODO:
Review the existing FlorvaLink app design (see attachments) and identify areas for visual improvement.
Provide a detailed UI style guide, including:
Typography (font choices, sizes, and weights)
Color palette (primary, secondary, and accent colors)
Component styling (buttons, forms, icons, and interactive elements)
Spacing and layout guidelines (margins, paddings, and alignment)
Ensure the design remains clean, modern, and professional while maintaining usability and accessibility.
Provide design mockups or visual examples (if possible) to illustrate the proposed changes.
Deliverables:
A UI Style Guide (PDF or Figma file) with specifications on fonts, colors, spacing, and UI components.
Optionally, before/after mockups or examples demonstrating the improvements.
Ideal Designer:
Strong experience in mobile UI/UX design.
Understanding of modern design trends and best practices.
Ability to communicate design choices clearly for easy developer implementation.
I have attached 7 images showcasing the main UI screens used in the FlorvaLink app. These screens need visual enhancements to improve their overall look and user experience.
The images represent the current design in three key modes:
LIST Mode – Displays data in a structured list format.
READ Mode – Shows detailed information when a user selects an item.
ADD/EDIT Mode – Allows users to input or modify information.
Additionally, there is a ‘MORE’ page, which serves as a menu listing other features of the application.
Task Objective:
Please refine and improve these UIs to create a more modern, visually appealing, and user-friendly experience. Focus on typography, colors, spacing, and component styling to ensure a cohesive and polished design.
Look and feel
Each slider illustrates characteristics of the customer's brand and the style your logo design should communicate.

```html
<!DOCTYPE html>
<html lang="en">
<head>
<meta charset="utf-8">
<title>UI Improvement for FlorvaLink App</title>
<link href="https://fonts.googleapis.com/css2?family=Inter:wght@400;500;600;700;800&display=swap" rel="stylesheet">
<style>
:root{
  --brand:#1552a6;
  --brand-deep:#0d449a;
  --brand-soft:#dbe8fa;
  --page:#ffffff;
  --screen-bg:#eef3fb;
  --card:#ffffff;
  --ink:#1d2433;
  --muted:#9aa3b2;
  --line:#e4e9f1;
  --icon-nav:#c3d2e8;
  --pilot:#fffbc4;
  --owner:#bfe2fb;
  --qualified:#b8f6a9;
  --tag-green:#12a55a;
  --tag-green-bg:#e6f8ee;
  --tag-blue:#1552a6;
  --tag-grey-bg:#eef0f3;
  --list-grey:#e2e8f1;
}
*{box-sizing:border-box;margin:0;padding:0}
html,body{width:851px;height:1200px;overflow:hidden;background:var(--page)}
body{font-family:'Inter',sans-serif;color:var(--ink)}
.board{position:absolute;left:0;top:0;width:1624px;height:2290px;transform:scale(.52401);transform-origin:0 0;background:var(--page)}
.hero-band{position:absolute;left:0;top:0;width:1624px;height:595px;background:linear-gradient(180deg,#0f4597 0%,#1a5ab0 55%,#1552a6 100%)}
.hero-title{position:absolute;left:0;width:1624px;top:128px;text-align:center;color:#fff;font-weight:800;font-size:50px;letter-spacing:.5px}
.closing{position:absolute;left:0;width:1624px;top:2118px;text-align:center;color:#111;font-weight:800;font-size:50px;letter-spacing:.5px}
.screen-label{position:absolute;width:300px;margin-left:-150px;text-align:center;font-weight:700;font-size:14px;letter-spacing:.3px}
.row-top .screen-label{color:#fff}
.screen-label.dark{color:#111}
.screen{position:absolute;width:250px;border-radius:34px;overflow:hidden;background:var(--screen-bg);box-shadow:0 0 0 1px #d5deeb}
.screen-head{position:absolute;left:0;top:0;width:100%;height:128px;background:linear-gradient(180deg,#0f4597,#1d5cb4)}
.status{position:absolute;top:12px;left:16px;right:16px;height:12px;color:#fff;font-size:8px;font-weight:500}
.status svg{position:absolute;right:0;top:0}
.topbar{position:absolute;top:43px;left:12px;right:12px;height:20px;color:#fff}
.topbar .back,.topbar .more{position:absolute;top:2px;width:16px;height:16px;border-radius:50%;background:rgba(255,255,255,.22);display:flex;align-items:center;justify-content:center}
.topbar .back{left:0}
.topbar .more{right:0}
.topbar .title{position:absolute;left:0;right:0;top:1px;text-align:center;font-size:13px;font-weight:600}
.topbar .save{position:absolute;right:24px;top:3px;width:36px;height:14px;border-radius:7px;background:rgba(255,255,255,.28);font-size:7px;text-align:center;line-height:14px}
.ico{width:22px;height:22px;fill:none;stroke:currentColor;stroke-width:1.6;stroke-linecap:round;stroke-linejoin:round}
.nav{position:absolute;left:0;right:0;bottom:0;height:52px;background:#fff}
.nav .pill{position:absolute;left:16px;top:13px;width:70px;height:26px;border-radius:13px;background:var(--brand-deep);color:#fff;font-size:8px;font-weight:500;display:flex;align-items:center;gap:5px;padding-left:11px}
.nav .pill .ico{width:11px;height:11px;stroke-width:2.2}
.nav .ni{position:absolute;top:17px;width:17px;height:17px;color:var(--icon-nav);stroke-width:2}
.card{position:absolute;left:10px;right:10px;background:var(--card);border-radius:10px}
.card-title{position:absolute;left:12px;font-size:11px;font-weight:500}
.field{position:absolute;left:12px;right:12px;height:38px;border:1px solid var(--line);border-radius:6px;background:#fff}
.field .ico{position:absolute;left:10px;top:10px;width:16px;height:16px;color:#a7b0bf}
.field .lbl{position:absolute;left:41px;top:8px;font-size:6.5px;color:var(--muted)}
.field .val{position:absolute;left:41px;top:20px;font-size:9px}
.field .star{color:var(--brand);font-size:7px}
.field .chev{position:absolute;right:10px;top:13px;width:11px;height:11px;color:#4b5567}
.section-title{position:absolute;left:18px;font-size:11px;font-weight:500}
.tile{position:absolute;width:110px;background:#fff;border-radius:14px;text-align:center;color:var(--brand)}
.tile .ico{position:absolute;left:50%;margin-left:-12px;width:24px;height:24px;stroke-width:1.5}
.tile .tlabel{position:absolute;left:4px;right:4px;font-size:8.5px;line-height:10.5px;color:var(--ink)}
.panel{position:absolute;left:8px;right:8px;border-radius:6px}
.panel .ptitle{position:absolute;left:9px;top:11px;font-size:8.5px;font-weight:500}
.select{position:absolute;left:8px;right:8px;background:#fff;border-radius:6px;font-size:7.5px;line-height:11px;padding:6px 22px 6px 10px;color:#333}
.select .chev{position:absolute;right:9px;top:50%;margin-top:-5px;width:10px;height:10px;color:#333}
.btn{position:absolute;left:8px;height:13px;border-radius:7px;background:var(--brand-deep);color:#fff;font-size:7px;font-weight:500;line-height:13px;padding:0 9px}
.drow{position:absolute;left:14px;right:14px;height:50px;border-bottom:1px solid #eef1f5}
.drow .badge{position:absolute;left:2px;top:11px;width:24px;height:24px;border-radius:50%;background:var(--brand-soft);color:var(--brand);display:flex;align-items:center;justify-content:center}
.drow .badge .ico{width:13px;height:13px}
.drow .lbl{position:absolute;left:41px;top:12px;font-size:6.5px;color:var(--muted)}
.drow .val{position:absolute;left:41px;top:25px;font-size:9px}
.action{position:absolute;left:8px;right:8px;height:34px;background:#fff;border-radius:6px;font-size:9px}
.action .badge{position:absolute;left:12px;top:7px;width:20px;height:20px;border-radius:50%;background:var(--brand-soft);color:var(--brand);display:flex;align-items:center;justify-content:center}
.action .badge .ico{width:12px;height:12px}
.action span{position:absolute;left:44px;top:11px}
.mtile{position:absolute;width:108px;background:#fff;border-radius:14px;color:var(--brand)}
.mtile .ico{position:absolute;left:50%;margin-left:-13px;top:18px;width:26px;height:26px;stroke-width:1.5}
.mtile .tlabel{position:absolute;left:0;right:0;text-align:center;font-size:9px;line-height:11px;color:var(--ink)}
.wbtn{position:absolute;top:12px;height:28px;border-radius:6px;background:#e4eefb;color:#3a4b66;font-size:9px;display:flex;align-items:center;gap:5px;padding:0 9px}
.wbtn .ico{width:12px;height:12px}
.search{position:absolute;left:12px;right:12px;height:34px;border:1px solid var(--line);border-radius:8px;font-size:9px;color:#555}
.search .ico{position:absolute;width:12px;height:12px;top:11px;color:#9aa3b2}
.search span{position:absolute;top:11px}
.filter{position:absolute;right:7px;top:7px;width:20px;height:20px;border-radius:50%;background:#1a73e8;color:#fff;display:flex;align-items:center;justify-content:center}
.filter .ico{width:11px;height:11px;stroke-width:2}
.letter{position:absolute;left:24px;font-size:10px;color:#333}
.letter .chev{position:absolute;left:190px;top:2px;width:10px;height:10px;color:#888}
.person{position:absolute;left:24px;right:24px;height:56px;border-bottom:1px solid #eef1f5}
.avatar{position:absolute;left:0;top:8px;width:38px;height:38px;border-radius:50%;background:linear-gradient(160deg,#8aa6c8,#2b3c55)}
.person .name{position:absolute;left:50px;top:10px;font-size:9.5px}
.person .num{position:absolute;left:50px;top:26px;height:12px;padding:0 7px;border-radius:6px;background:var(--brand-soft);color:var(--brand);font-size:7px;line-height:12px}
.person .date{position:absolute;right:0;top:28px;font-size:7.5px;color:#aab1bd}
.chips{position:absolute;left:12px;top:139px;display:flex;gap:6px}
.chip{height:13px;padding:0 7px;border-radius:7px;font-size:7px;line-height:13px;color:#555;background:#fff}
.chip.on{background:var(--brand-deep);color:#fff;padding:0 8px}
.cperson{position:absolute;left:12px;right:12px;height:58px;border-bottom:1px solid #eef1f5}
.cperson .avatar{left:4px;width:36px;height:36px;top:9px}
.cperson .name{position:absolute;left:52px;top:10px;font-size:9.5px}
.tags{position:absolute;left:52px;top:28px;display:flex;gap:5px}
.tag{height:13px;padding:0 7px;border-radius:7px;font-size:6.5px;line-height:13px;font-weight:500}
.tag.green{background:var(--tag-green-bg);color:var(--tag-green)}
.tag.blue{background:var(--brand-soft);color:var(--tag-blue)}
.tag.grey{background:var(--tag-grey-bg);color:#555}
</style>
</head>
<body>
<svg width="0" height="0" style="position:absolute" aria-hidden="true">
  <symbol id="i-user" viewBox="0 0 24 24"><circle cx="12" cy="8" r="4"/><path d="M4 21c0-4 4-6 8-6s8 2 8 6"/></symbol>
  <symbol id="i-bag" viewBox="0 0 24 24"><rect x="3" y="7" width="18" height="13" rx="2"/><path d="M8 7V5h8v2M3 12h18M11 12v2h2v-2"/></symbol>
  <symbol id="i-pin" viewBox="0 0 24 24"><path d="M12 21s-7-6-7-11a7 7 0 0 1 14 0c0 5-7 11-7 11z"/><circle cx="12" cy="10" r="2.5"/></symbol>
  <symbol id="i-city" viewBox="0 0 24 24"><rect x="4" y="4" width="9" height="17"/><rect x="13" y="10" width="7" height="11"/><path d="M7 8h3M7 12h3M7 16h3M16 14h1M16 17h1"/></symbol>
  <symbol id="i-chev" viewBox="0 0 24 24"><path d="M6 9l6 6 6-6"/></symbol>
  <symbol id="i-back" viewBox="0 0 24 24"><path d="M14 6l-6 6 6 6"/></symbol>
  <symbol id="i-dots" viewBox="0 0 24 24"><circle cx="6" cy="12" r="1"/><circle cx="12" cy="12" r="1"/><circle cx="18" cy="12" r="1"/></symbol>
  <symbol id="i-bulb" viewBox="0 0 24 24"><circle cx="12" cy="10" r="5"/><circle cx="12" cy="10" r="2"/><path d="M10 17h4M10 20h4M12 2v1M4 10H3M21 10h-1M6 4l1 1M18 4l-1 1"/></symbol>
  <symbol id="i-help" viewBox="0 0 24 24"><rect x="5" y="3" width="14" height="18" rx="2"/><path d="M10 9a2 2 0 1 1 2 2v2M12 16v.5"/></symbol>
  <symbol id="i-plane" viewBox="0 0 24 24"><path d="M21 3L3 10l7 3 3 7z"/><path d="M10 13l4-4"/></symbol>
  <symbol id="i-login" viewBox="0 0 24 24"><circle cx="12" cy="12" r="9"/><path d="M7 12h9M13 9l3 3-3 3"/></symbol>
  <symbol id="i-target" viewBox="0 0 24 24"><circle cx="12" cy="12" r="9"/><circle cx="12" cy="11" r="3"/><path d="M7 18c1-2 3-3 5-3s4 1 5 3"/></symbol>
  <symbol id="i-cal" viewBox="0 0 24 24"><rect x="3" y="5" width="18" height="16" rx="2"/><path d="M3 10h18M8 3v4M16 3v4M9 15l2 2 4-4"/></symbol>
  <symbol id="i-users" viewBox="0 0 24 24"><circle cx="8" cy="8" r="3"/><circle cx="16" cy="8" r="3"/><path d="M2 20c0-3 3-5 6-5s6 2 6 5M14 15c3 0 8 1 8 5"/></symbol>
  <symbol id="i-dash" viewBox="0 0 24 24"><rect x="3" y="4" width="18" height="13" rx="1"/><path d="M8 21h8M12 17v4M7 14v-3M10 14V9M13 14v-2"/><circle cx="16" cy="10" r="2"/></symbol>
  <symbol id="i-track" viewBox="0 0 24 24"><circle cx="12" cy="12" r="9"/><path d="M12 7a5 5 0 1 0 5 5"/><circle cx="12" cy="12" r="1.5"/></symbol>
  <symbol id="i-star" viewBox="0 0 24 24"><path d="M12 3l2.5 5 5.5.8-4 3.9 1 5.5L12 15.6 7 18.2l1-5.5-4-3.9 5.5-.8z"/><path d="M4 21h16"/></symbol>
  <symbol id="i-tool" viewBox="0 0 24 24"><rect x="3" y="4" width="18" height="16" rx="2"/><path d="M3 8h18M9 12l3 3 3-3M12 15v-4"/></symbol>
  <symbol id="i-gear" viewBox="0 0 24 24"><circle cx="12" cy="12" r="3"/><path d="M12 2l2 3 3-1 1 3 3 1-1 3 2 2-2 2 1 3-3 1-1 3-3-1-2 3-2-3-3 1-1-3-3-1 1-3-2-2 2-2-1-3 3-1 1-3 3 1z"/></symbol>
  <symbol id="i-print" viewBox="0 0 24 24"><rect x="6" y="3" width="12" height="5"/><rect x="3" y="8" width="18" height="9" rx="2"/><rect x="7" y="14" width="10" height="7"/></symbol>
  <symbol id="i-plus" viewBox="0 0 24 24"><circle cx="12" cy="12" r="9"/><path d="M12 8v8M8 12h8"/></symbol>
  <symbol id="i-search" viewBox="0 0 24 24"><circle cx="11" cy="11" r="6"/><path d="M16 16l5 5"/></symbol>
  <symbol id="i-filter" viewBox="0 0 24 24"><path d="M4 5h16l-6 8v6l-4-2v-4z"/></symbol>
  <symbol id="i-chat" viewBox="0 0 24 24"><path d="M4 4h16v12H10l-6 5z"/></symbol>
  <symbol id="i-doc" viewBox="0 0 24 24"><rect x="5" y="3" width="14" height="18" rx="2"/><path d="M9 8h6M9 12h6M9 16h4"/></symbol>
  <symbol id="i-grid" viewBox="0 0 24 24"><rect x="3" y="3" width="7" height="7" rx="2"/><rect x="14" y="3" width="7" height="7" rx="2"/><rect x="3" y="14" width="7" height="7" rx="2"/><rect x="14" y="14" width="7" height="7" rx="2"/></symbol>
  <symbol id="i-shield" viewBox="0 0 24 24"><path d="M12 3l8 3v6c0 5-4 8-8 9-4-1-8-4-8-9V6z"/><path d="M9 12l2 2 4-4"/></symbol>
  <symbol id="i-cert" viewBox="0 0 24 24"><rect x="4" y="3" width="16" height="18" rx="2"/><circle cx="12" cy="10" r="3"/><path d="M9 17h6"/></symbol>
  <symbol id="i-cap" viewBox="0 0 24 24"><ellipse cx="12" cy="14" rx="9" ry="4"/><path d="M6 13c0-3 3-6 6-6s6 3 6 6M9 14h6"/></symbol>
  <symbol id="i-status" viewBox="0 0 40 12"><path d="M1 10h2M4 10V7M7 10V4" stroke="#fff" stroke-width="1.4"/><path d="M14 5a6 6 0 0 1 8 0M16 7.5a3 3 0 0 1 4 0" stroke="#fff" stroke-width="1.3" fill="none"/><circle cx="18" cy="10" r="1" fill="#fff"/><rect x="26" y="3" width="12" height="7" rx="1.5" stroke="#fff" fill="none"/><rect x="27.5" y="4.5" width="9" height="4" fill="#fff"/></symbol>
</svg>

<div class="board">
  <div class="hero-band" role="img" aria-label="Airport apron with parked aircraft in a blue duotone"></div>
  <h1 class="hero-title">UI IMPROVEMENT FOR FLORVALINK APP</h1>

  <div class="row-top">
    <div class="screen-label" style="left:281px;top:305px">RADS_ADDEDIT_PAGE</div>
    <div class="screen-label" style="left:628px;top:305px">RADS_READ_PAGE</div>
    <div class="screen-label" style="left:992px;top:305px">RADS_READ_PAGE2</div>
    <div class="screen-label" style="left:1339px;top:305px">RADS_READ_PAGE3</div>
  </div>
  <div class="screen-label dark" style="left:256px;top:1281px">RADS_MORE_PAGE</div>
  <div class="screen-label dark" style="left:640px;top:1281px">RADS_READ_PAGE3</div>
  <div class="screen-label dark" style="left:1007px;top:1281px">RADS_MORE_PAGE</div>
  <div class="screen-label dark" style="left:1378px;top:1281px">RADS_READ_PAGE3</div>

  <!-- Add / edit contact -->
  <section class="screen" style="left:157px;top:360px;height:655px">
    <div class="screen-head"></div>
    <div class="status">12:30PM<svg width="40" height="12"><use href="#i-status"/></svg></div>
    <div class="topbar"><div class="back"><svg class="ico" style="width:10px;height:10px"><use href="#i-back"/></svg></div><div class="title">Add Contact</div><div class="save">Save</div><div class="more"><svg class="ico" style="width:10px;height:10px;stroke-width:3"><use href="#i-dots"/></svg></div></div>
    <div class="card" style="top:81px;height:514px">
      <div class="card-title" style="top:16px">Contact Information</div>
      <svg class="ico" style="position:absolute;right:12px;top:14px;width:14px;height:14px;color:#aaa;stroke-width:3"><use href="#i-dots"/></svg>
      <div class="field" style="top:43px"><svg class="ico"><use href="#i-bag"/></svg><div class="lbl">Business Name - e</div><div class="val">Contact Business name</div></div>
      <div class="field" style="top:91px"><svg class="ico"><use href="#i-user"/></svg><div class="lbl">First Name -e</div><div class="val">Marcus</div></div>
      <div class="field" style="top:139px"><svg class="ico"><use href="#i-user"/></svg><div class="lbl">Middle Name -e</div><div class="val">Peter</div></div>
      <div class="field" style="top:187px"><svg class="ico"><use href="#i-user"/></svg><div class="lbl">Last Name -e</div><div class="val">Jensen</div></div>
      <div class="section-title" style="top:243px;left:18px">Address Information</div>
      <svg class="ico" style="position:absolute;right:14px;top:246px;width:11px;height:11px;color:var(--brand)"><use href="#i-chev"/></svg>
      <div class="field" style="top:270px"><svg class="ico"><use href="#i-pin"/></svg><div class="lbl">Address Label Tag -e</div><div class="val">Address</div><svg class="ico chev"><use href="#i-chev"/></svg></div>
      <div class="field" style="top:318px"><svg class="ico"><use href="#i-pin"/></svg><div class="lbl">Address Line1 -e <span class="star">★</span></div><div class="val">Marcus</div></div>
      <div class="field" style="top:366px"><svg class="ico"><use href="#i-pin"/></svg><div class="lbl">Address Line2 -e <span class="star">★</span></div><div class="val">Peter</div></div>
      <div class="field" style="top:414px"><svg class="ico"><use href="#i-city"/></svg><div class="lbl">Address City</div><div class="val">New York City, NY</div></div>
      <div class="field" style="top:462px;right:88px"><div class="lbl" style="left:11px">AddressState</div><div class="val" style="left:11px">New York</div><svg class="ico chev"><use href="#i-chev"/></svg></div>
      <div class="field" style="top:462px;left:142px"><div class="lbl" style="left:10px">Zip -e</div><div class="val" style="left:10px">10021</div></div>
    </div>
    <nav class="nav"><div class="pill"><svg class="ico"><use href="#i-user"/></svg>Contact</div><svg class="ico ni" style="left:104px"><use href="#i-chat"/></svg><svg class="ico ni" style="left:142px"><use href="#i-bag"/></svg><svg class="ico ni" style="left:180px"><use href="#i-doc"/></svg><svg class="ico ni" style="left:217px"><use href="#i-grid"/></svg></nav>
  </section>

  <!-- Contact read -->
  <section class="screen" style="left:505px;top:360px;height:690px">
    <div class="screen-head"></div>
    <div class="status">12:30PM<svg width="40" height="12"><use href="#i-status"/></svg></div>
    <div class="topbar"><div class="back"><svg class="ico" style="width:10px;height:10px"><use href="#i-back"/></svg></div><div class="title" style="top:-1px">Contact</div><div class="more"><svg class="ico" style="width:10px;height:10px;stroke-width:3"><use href="#i-dots"/></svg></div></div>
    <div class="tile" style="left:8px;top:79px;height:103px"><svg class="ico" style="top:24px"><use href="#i-user"/></svg><div class="tlabel" style="top:64px">Add Personal<br>Information -e</div></div>
    <div class="tile" style="left:131px;top:79px;height:103px"><svg class="ico" style="top:24px"><use href="#i-bag"/></svg><div class="tlabel" style="top:64px">Add Work<br>Info-e</div></div>
    <div class="tile" style="left:8px;top:194px;height:103px"><svg class="ico" style="top:24px"><use href="#i-bulb"/></svg><div class="tlabel" style="top:64px">Add Skills /<br>Talents -e</div></div>
    <div class="tile" style="left:131px;top:194px;height:103px"><svg class="ico" style="top:24px"><use href="#i-help"/></svg><div class="tlabel" style="top:64px">Add<br>Resources -e</div></div>
    <div class="panel" style="top:308px;height:69px;background:var(--pilot)"><div class="ptitle">Pilots -e</div><div class="select" style="top:30px">Ashby, Colin, 3647946, 10/31/23<svg class="ico chev"><use href="#i-chev"/></svg></div></div>
    <div class="panel" style="top:390px;height:108px;background:var(--owner)"><div class="ptitle">Aircraft Owner -e</div><div class="select" style="top:30px">Ashby, Colin: Aerilon: 182T: Aerilon<br>Aircraft Company, Single Engine, 1100<svg class="ico chev"><use href="#i-chev"/></svg></div><div class="btn" style="top:84px">Add Aircraft Owner</div></div>
    <div class="panel" style="top:511px;height:108px;background:var(--qualified)"><div class="ptitle">Qualified Pilot -e</div><div class="select" style="top:30px">Ashby, Colin: Aerilon: 182T: Aerilon<br>Aircraft Company, Single Engine, 1100<svg class="ico chev"><use href="#i-chev"/></svg></div><div class="btn" style="top:84px">Add Qualified Pilot -e</div></div>
    <nav class="nav"><div class="pill"><svg class="ico"><use href="#i-user"/></svg>Contact</div><svg class="ico ni" style="left:104px"><use href="#i-chat"/></svg><svg class="ico ni" style="left:142px"><use href="#i-bag"/></svg><svg class="ico ni" style="left:180px"><use href="#i-doc"/></svg><svg class="ico ni" style="left:217px"><use href="#i-grid"/></svg></nav>
  </section>

  <!-- Contact read, extended -->
  <section class="screen" style="left:859px;top:360px;height:852px">
    <div class="screen-head"></div>
    <div class="status">12:30PM<svg width="40" height="12"><use href="#i-status"/></svg></div>
    <div class="topbar"><div class="back"><svg class="ico" style="width:10px;height:10px"><use href="#i-back"/></svg></div><div class="title" style="top:-1px">Contact</div><div class="more"><svg class="ico" style="width:10px;height:10px;stroke-width:3"><use href="#i-dots"/></svg></div></div>
    <div class="tile" style="left:8px;top:79px;height:102px"><svg class="ico" style="top:20px"><use href="#i-user"/></svg><div class="tlabel" style="top:60px">Add<br>Email -e</div></div>
    <div class="tile" style="left:131px;top:79px;height:102px"><svg class="ico" style="top:20px"><use href="#i-bag"/></svg><div class="tlabel" style="top:60px">Add Social<br>Media -e</div></div>
    <div class="tile" style="left:8px;top:185px;height:102px"><svg class="ico" style="top:20px"><use href="#i-user"/></svg><div class="tlabel" style="top:60px">Add<br>Email -e</div></div>
    <div class="tile" style="left:131px;top:185px;height:102px"><svg class="ico" style="top:20px"><use href="#i-bag"/></svg><div class="tlabel" style="top:60px">Add Social<br>Media -e</div></div>
    <div class="tile" style="left:8px;top:291px;height:102px"><svg class="ico" style="top:20px"><use href="#i-bulb"/></svg><div class="tlabel" style="top:60px">Add Emergency<br>Contact -e</div></div>
    <div class="tile" style="left:131px;top:291px;height:102px"><svg class="ico" style="top:20px"><use href="#i-help"/></svg><div class="tlabel" style="top:60px">Add<br>Resources -e</div></div>
    <div class="tile" style="left:8px;right:8px;width:auto;top:398px;height:54px"><svg class="ico" style="left:52px;margin-left:0;top:15px"><use href="#i-bulb"/></svg><div class="tlabel" style="top:22px;left:88px;text-align:left;font-size:9px">Add Emergency Contact -e</div></div>
    <div class="panel" style="top:465px;height:70px;background:var(--pilot)"><div class="ptitle">Pilots -e</div><div class="select" style="top:30px">Ashby, Colin, 3647946, 10/31/23<svg class="ico chev"><use href="#i-chev"/></svg></div></div>
    <div class="panel" style="top:548px;height:109px;background:var(--owner)"><div class="ptitle">Aircraft Owner -e</div><div class="select" style="top:30px">Ashby, Colin: Aerilon: 182T: Aerilon<br>Aircraft Company, Single Engine, 1100<svg class="ico chev"><use href="#i-chev"/></svg></div><div class="btn" style="top:85px">Add Aircraft Owner</div></div>
    <div class="panel" style="top:669px;height:109px;background:var(--qualified)"><div class="ptitle">Qualified Pilot -e</div><div class="select" style="top:30px">Ashby, Colin: Aerilon: 182T: Aerilon<br>Aircraft Company, Single Engine, 1100<svg class="ico chev"><use href="#i-chev"/></svg></div><div class="btn" style="top:85px">Add Qualified Pilot -e</div></div>
    <nav class="nav"><div class="pill"><svg class="ico"><use href="#i-user"/></svg>Contact</div><svg class="ico ni" style="left:104px"><use href="#i-chat"/></svg><svg class="ico ni" style="left:142px"><use href="#i-bag"/></svg><svg class="ico ni" style="left:180px"><use href="#i-doc"/></svg><svg class="ico ni" style="left:217px"><use href="#i-grid"/></svg></nav>
  </section>

  <!-- Pilot read -->
  <section class="screen" style="left:1206px;top:360px;height:785px">
    <div class="screen-head"></div>
    <div class="status">12:30PM<svg width="40" height="12"><use href="#i-status"/></svg></div>
    <div class="topbar"><div class="back"><svg class="ico" style="width:10px;height:10px"><use href="#i-back"/></svg></div><div class="title" style="top:-1px">Pilot</div><div class="more"><svg class="ico" style="width:10px;height:10px;stroke-width:3"><use href="#i-dots"/></svg></div></div>
    <div class="card" style="top:75px;height:317px;left:8px;right:8px">
      <div class="card-title" style="top:16px">Details</div>
      <div class="drow" style="top:42px"><div class="badge"><svg class="ico"><use href="#i-cap"/></svg></div><div class="lbl">Pilot - e</div><div class="val">Alder, Connor, Blake</div></div>
      <div class="drow" style="top:96px"><div class="badge"><svg class="ico"><use href="#i-cert"/></svg></div><div class="lbl">Pilot Certificate No -e</div><div class="val">3182133</div></div>
      <div class="drow" style="top:150px"><div class="badge"><svg class="ico"><use href="#i-shield"/></svg></div><div class="lbl">Medical Expiration Date -e</div><div class="val">9/30/24</div></div>
      <div class="drow" style="top:204px"><div class="badge"><svg class="ico"><use href="#i-cal"/></svg></div><div class="lbl">Flight Review Expiration Date -e</div><div class="val">6/30/24</div></div>
      <div class="drow" style="top:258px"><div class="badge"><svg class="ico"><use href="#i-plane"/></svg></div><div class="lbl">Total Flight Time -e</div><div class="val">2500</div></div>
    </div>
    <div class="card" style="top:401px;height:142px;left:8px;right:8px">
      <div class="select" style="top:10px;background:#eef3fb;padding:8px 22px 8px 10px">Ashby, Colin: Aerilon: 182T: Aerilon<br>Aircraft Company, Single Engine, 1100<svg class="ico chev"><use href="#i-chev"/></svg></div>
      <div class="select" style="top:63px;background:#eef3fb;padding:8px 22px 8px 10px">Ashby, Colin: Aerilon: 182T: Aerilon<br>Aircraft Company, Single Engine, 1100<svg class="ico chev"><use href="#i-chev"/></svg></div>
      <div class="btn" style="top:119px;right:8px;text-align:center;height:15px;line-height:15px">Add Base Airport -e</div>
    </div>
    <div class="action" style="top:558px;height:34px"><div class="badge"><svg class="ico"><use href="#i-bulb"/></svg></div><span>Add Ratings -s</span></div>
    <div class="card" style="top:603px;height:200px;left:8px;right:8px">
      <div class="card-title" style="top:16px">Details</div>
      <div class="drow" style="top:42px"><div class="badge"><svg class="ico"><use href="#i-cap"/></svg></div><div class="lbl">Pilot - e</div><div class="val">Alder, Connor, Blake</div></div>
      <div class="drow" style="top:96px"><div class="badge"><svg class="ico"><use href="#i-cert"/></svg></div><div class="lbl">Pilot Certificate No -e</div><div class="val">3182133</div></div>
    </div>
    <nav class="nav"><div class="pill"><svg class="ico"><use href="#i-user"/></svg>Contact</div><svg class="ico ni" style="left:104px"><use href="#i-chat"/></svg><svg class="ico ni" style="left:142px"><use href="#i-bag"/></svg><svg class="ico ni" style="left:180px"><use href="#i-doc"/></svg><svg class="ico ni" style="left:217px"><use href="#i-grid"/></svg></nav>
  </section>

  <!-- More menu -->
  <section class="screen" style="left:125px;top:1337px;height:598px">
    <div class="screen-head"></div>
    <div class="status">12:30PM<svg width="40" height="12"><use href="#i-status"/></svg></div>
    <div class="topbar"><div class="title" style="top:-1px">More</div><div class="more"><svg class="ico" style="width:10px;height:10px;stroke-width:3"><use href="#i-dots"/></svg></div></div>
    <div class="mtile" style="left:10px;top:78px;height:80px"><svg class="ico"><use href="#i-plane"/></svg><div class="tlabel" style="top:58px">Flight</div></div>
    <div class="mtile" style="left:132px;top:78px;height:80px"><svg class="ico"><use href="#i-login"/></svg><div class="tlabel" style="top:58px">Login</div></div>
    <div class="mtile" style="left:10px;top:168px;height:80px"><svg class="ico"><use href="#i-target"/></svg><div class="tlabel" style="top:58px">Account</div></div>
    <div class="mtile" style="left:132px;top:168px;height:80px"><svg class="ico"><use href="#i-cal"/></svg><div class="tlabel" style="top:58px">Calendar</div></div>
    <div class="mtile" style="left:10px;top:258px;height:80px"><svg class="ico"><use href="#i-users"/></svg><div class="tlabel" style="top:58px">Users</div></div>
    <div class="mtile" style="left:132px;top:258px;height:80px"><svg class="ico"><use href="#i-dash"/></svg><div class="tlabel" style="top:58px">Dashboard</div></div>
    <div class="mtile" style="left:10px;top:348px;height:82px"><svg class="ico"><use href="#i-track"/></svg><div class="tlabel" style="top:60px">Tracking</div></div>
    <div class="mtile" style="left:132px;top:348px;height:82px"><svg class="ico"><use href="#i-star"/></svg><div class="tlabel" style="top:60px">Outreach Event</div></div>
    <div class="mtile" style="left:10px;top:440px;height:92px"><svg class="ico"><use href="#i-tool"/></svg><div class="tlabel" style="top:58px">Maintenance<br>Resources</div></div>
    <div class="mtile" style="left:132px;top:440px;height:92px"><svg class="ico"><use href="#i-gear"/></svg><div class="tlabel" style="top:64px">Settings</div></div>
    <nav class="nav"><div class="pill"><svg class="ico"><use href="#i-user"/></svg>Contact</div><svg class="ico ni" style="left:104px"><use href="#i-chat"/></svg><svg class="ico ni" style="left:142px"><use href="#i-bag"/></svg><svg class="ico ni" style="left:180px"><use href="#i-doc"/></svg><svg class="ico ni" style="left:217px"><use href="#i-grid"/></svg></nav>
  </section>

  <!-- Work order read -->
  <section class="screen" style="left:505px;top:1337px;height:598px">
    <div class="screen-head"></div>
    <div class="status">12:30PM<svg width="40" height="12"><use href="#i-status"/></svg></div>
    <div class="topbar"><div class="back"><svg class="ico" style="width:10px;height:10px"><use href="#i-back"/></svg></div><div class="title" style="top:-1px">Work Order</div><div class="more"><svg class="ico" style="width:10px;height:10px;stroke-width:3"><use href="#i-dots"/></svg></div></div>
    <div class="card" style="top:72px;height:366px;left:8px;right:8px">
      <div class="wbtn" style="left:12px"><svg class="ico"><use href="#i-print"/></svg>Print</div>
      <div class="wbtn" style="left:78px"><svg class="ico"><use href="#i-plus"/></svg>Create</div>
      <div class="wbtn" style="left:152px"><svg class="ico"><use href="#i-plus"/></svg>Create</div>
      <div class="card-title" style="top:56px">Details</div>
      <div class="drow" style="top:82px"><div class="badge"><svg class="ico"><use href="#i-cap"/></svg></div><div class="lbl">Pilot - e</div><div class="val">Alder, Connor, Blake</div></div>
      <div class="drow" style="top:136px"><div class="badge"><svg class="ico"><use href="#i-cert"/></svg></div><div class="lbl">Pilot Certificate No -e</div><div class="val">3182133</div></div>
      <div class="drow" style="top:190px"><div class="badge"><svg class="ico"><use href="#i-shield"/></svg></div><div class="lbl">Medical Expiration Date -e</div><div class="val">9/30/24</div></div>
      <div class="drow" style="top:244px"><div class="badge"><svg class="ico"><use href="#i-cal"/></svg></div><div class="lbl">Flight Review Expiration Date -e</div><div class="val">6/30/24</div></div>
      <div class="drow" style="top:298px"><div class="badge"><svg class="ico"><use href="#i-plane"/></svg></div><div class="lbl">Total Flight Time -e</div><div class="val">2500</div></div>
    </div>
    <div class="action" style="top:442px"><div class="badge"><svg class="ico"><use href="#i-user"/></svg></div><span>Add Technician -e</span></div>
    <div class="action" style="top:491px"><div class="badge"><svg class="ico"><use href="#i-doc"/></svg></div><span>Add Line Items -e</span></div>
    <nav class="nav"><div class="pill"><svg class="ico"><use href="#i-user"/></svg>Contact</div><svg class="ico ni" style="left:104px"><use href="#i-chat"/></svg><svg class="ico ni" style="left:142px"><use href="#i-bag"/></svg><svg class="ico ni" style="left:180px"><use href="#i-doc"/></svg><svg class="ico ni" style="left:217px"><use href="#i-grid"/></svg></nav>
  </section>

  <!-- Pilots list -->
  <section class="screen" style="left:876px;top:1337px;height:615px">
    <div class="screen-head"></div>
    <div class="status">12:30PM<svg width="40" height="12"><use href="#i-status"/></svg></div>
    <div class="topbar" style="top:45px"><div class="back"><svg class="ico" style="width:10px;height:10px"><use href="#i-back"/></svg></div><div class="title">Pilots</div><div class="save">Save</div><div class="more"><svg class="ico" style="width:10px;height:10px;stroke-width:3"><use href="#i-dots"/></svg></div></div>
    <div class="card" style="top:80px;height:475px;left:8px;right:8px">
      <div class="search" style="top:12px"><svg class="ico" style="left:10px"><use href="#i-search"/></svg><span style="left:30px">Search</span><div class="filter"><svg class="ico"><use href="#i-filter"/></svg></div></div>
    </div>
    <div class="letter" style="top:140px">A<svg class="ico chev"><use href="#i-chev"/></svg></div>
    <div class="person" style="top:164px"><div class="avatar" role="img" aria-label="Pilot portrait photo"></div><div class="name">Alder, Connor Blake</div><div class="num">3182133</div><div class="date">9/30/24</div></div>
    <div class="person" style="top:226px"><div class="avatar" role="img" aria-label="Pilot portrait photo"></div><div class="name">Aberline, Victor Shane</div><div class="num">4467155</div><div class="date">5/19/24</div></div>
    <div class="person" style="top:288px"><div class="avatar" role="img" aria-label="Pilot portrait photo"></div><div class="name">Ardent, Lena, Rose</div><div class="num">4360575</div><div class="date">2/25/25</div></div>
    <div class="letter" style="top:356px">B<svg class="ico chev"><use href="#i-chev"/></svg></div>
    <div class="person" style="top:380px"><div class="avatar" role="img" aria-label="Pilot portrait photo"></div><div class="name">Birchwell, Owen, Hale</div><div class="num">4360575</div><div class="date">9/30/24</div></div>
    <div class="person" style="top:443px;border:none"><div class="avatar" role="img" aria-label="Pilot portrait photo"></div><div class="name">Bastow, Rowan</div><div class="num">3423819</div><div class="date">2/28/25</div></div>
    <div class="letter" style="top:513px">C<svg class="ico chev"><use href="#i-chev"/></svg></div>
    <nav class="nav"><div class="pill"><svg class="ico"><use href="#i-user"/></svg>Contact</div><svg class="ico ni" style="left:104px"><use href="#i-chat"/></svg><svg class="ico ni" style="left:142px"><use href="#i-bag"/></svg><svg class="ico ni" style="left:180px"><use href="#i-doc"/></svg><svg class="ico ni" style="left:217px"><use href="#i-grid"/></svg></nav>
  </section>

  <!-- Contact list -->
  <section class="screen" style="left:1245px;top:1337px;height:615px;background:var(--list-grey)">
    <div class="screen-head"></div>
    <div class="status">12:30PM<svg width="40" height="12"><use href="#i-status"/></svg></div>
    <div class="topbar" style="top:45px"><div class="back"><svg class="ico" style="width:10px;height:10px"><use href="#i-back"/></svg></div><div class="title">Contact</div><div class="save">Save</div><div class="more"><svg class="ico" style="width:10px;height:10px;stroke-width:3"><use href="#i-dots"/></svg></div></div>
    <div class="card" style="top:80px;height:380px;left:6px;right:6px">
      <div class="search" style="top:12px;background:#f7f9fc;border-color:#f0f2f6"><span style="left:12px">Search</span><svg class="ico" style="right:10px"><use href="#i-search"/></svg></div>
      <div class="chips" style="top:57px"><div class="chip on">All</div><div class="chip">Aircraft Owner</div><div class="chip">Enthusiast -e</div><div class="chip">Pilot</div></div>
      <div class="cperson" style="top:74px"><div class="avatar" role="img" aria-label="Contact portrait photo"></div><div class="name">Alder, Connor Blake</div><div class="tags"><div class="tag green">Aircraft Owner</div><div class="tag blue">Enthusiast -e</div></div></div>
      <div class="cperson" style="top:134px"><div class="avatar" role="img" aria-label="Contact portrait photo"></div><div class="name">Aberline, Victor Shane</div><div class="tags"><div class="tag green">Aircraft Owner</div><div class="tag green">Qualified Pilot</div><div class="tag grey">Pilot</div></div></div>
      <div class="cperson" style="top:194px"><div class="avatar" role="img" aria-label="Contact portrait photo"></div><div class="name">Gorvin, Cole, Yaret</div><div class="tags"><div class="tag green">Aircraft Owner</div><div class="tag green">Qualified Pilot</div><div class="tag grey">Pilot</div></div></div>
      <div class="cperson" style="top:254px"><div class="avatar" role="img" aria-label="Contact portrait photo"></div><div class="name">Gaspard, Jonah, Ellis</div><div class="tags"><div class="tag green">Aircraft Owner</div><div class="tag green">Qualified Pilot</div><div class="tag grey">Pilot</div></div></div>
      <div class="cperson" style="top:314px;border:none"><div class="avatar" role="img" aria-label="Contact portrait photo"></div><div class="name">Ardent, Lena, Rose</div><div class="tags"><div class="tag green">Aircraft Owner</div><div class="tag green">Qualified Pilot</div></div></div>
    </div>
    <nav class="nav"><div class="pill"><svg class="ico"><use href="#i-user"/></svg>Contact</div><svg class="ico ni" style="left:104px"><use href="#i-chat"/></svg><svg class="ico ni" style="left:142px"><use href="#i-bag"/></svg><svg class="ico ni" style="left:180px"><use href="#i-doc"/></svg><svg class="ico ni" style="left:217px"><use href="#i-grid"/></svg></nav>
  </section>

  <p class="closing">THANKS FOR WATCHING MY WORK</p>
</div>
</body>
</html>
```